pharmacy/travel clinic business card design

We need a business card for our new business called Brenwick Travel Clinic and Pharmacy. Our primary focus is doing consultations for people before travelling internationally and providing vaccinations and prescriptions for them. While the business is considered a pharmacy, it has more the look and feel of a doctor's office. The design should communicate a professional and trustworthy feel. I have attached a copy of the logo we are going to be using.
Updates
Thanks for the submissions.  If you haven`t been eliminated you are one of the finalists.  Decision will likely be made tomorrow.

Target Market(s)
Customers, other health care professionals, travel agents
Industry/Entity Type
Clinic
Look and feel
Each slider illustrates characteristics of the customer's brand and the style your logo design should communicate.

```html
<!DOCTYPE html>
<html lang="en">
<head>
<meta charset="utf-8">
<title>Brenwick Travel Clinic and Pharmacy – Business Card</title>
<link rel="stylesheet" href="https://fonts.googleapis.com/css2?family=Mulish:ital,wght@0,400;0,600;0,700;1,700&display=swap">
<style>
  :root {
    --bg: #e8e7e3;
    --card: #fbfbfa;
    --blue: #1d8fd2;
    --green: #7bbb2e;
    --ink: #2f3236;
    --shadow: rgba(0,0,0,0.14);
  }
  * { box-sizing: border-box; margin: 0; padding: 0; }
  html, body {
    width: 1200px; height: 1200px; overflow: hidden;
    background: var(--bg);
    font-family: "Mulish", sans-serif;
    color: var(--ink);
  }
  .sheet { position: relative; width: 1200px; height: 1200px; }
  .card {
    position: absolute; left: 240px;
    width: 720px; height: 411px;
    background: var(--card);
    box-shadow: 0 10px 28px var(--shadow);
  }
  .card--front { top: 120px; }
  .card--back  { top: 640px; }

  .brand-name {
    font-family: "Mulish", sans-serif;
    font-weight: 700;
    color: var(--blue);
    line-height: 1.05;
    display: flex; align-items: center; gap: 12px;
  }
  .brand-name .mark {
    width: 18px; height: 18px; border-radius: 50%;
    background: var(--blue); flex: none;
  }
  .card--front .brand-name {
    position: absolute; left: 120px; top: 120px;
    font-size: 52px;
  }
  .card--front .brand-name small,
  .card--back .brand-name small {
    display: block; font-size: 0.42em; letter-spacing: 0.04em;
  }

  .holder { position: absolute; left: 40px; top: 34px; }
  .holder-name { font-size: 24px; font-weight: 700; font-style: italic; color: var(--blue); }
  .holder-role { font-size: 18px; color: var(--green); margin-top: 2px; }

  .card--back .brand-name {
    position: absolute; left: 250px; top: 120px;
    font-size: 34px;
  }
  .divider {
    position: absolute; left: 0; top: 270px; width: 600px; height: 5px;
    background: linear-gradient(to right, var(--green) 60%, rgba(123,187,46,0));
  }
  .contacts {
    position: absolute; left: 40px; top: 290px; right: 40px;
    display: grid; grid-template-columns: 1fr 1fr; row-gap: 6px; column-gap: 20px;
    font-size: 19px;
  }
  .contacts .wide { grid-column: 1 / 3; }
  .contact { display: flex; align-items: center; gap: 8px; }
  .contact svg { width: 18px; height: 18px; flex: none; fill: var(--blue); }
</style>
</head>
<body>
<main class="sheet">

  <section class="card card--front" aria-label="Card front">
    <div class="brand-name"><span class="mark"></span><span>Brenwick<br>Travel Clinic<small>and PHARMACY</small></span></div>
  </section>

  <section class="card card--back" aria-label="Card back">
    <div class="holder">
      <p class="holder-name">Firstname Lastname</p>
      <p class="holder-role">Function</p>
    </div>

    <div class="brand-name"><span class="mark"></span><span>Brenwick<br>Travel Clinic<small>and PHARMACY</small></span></div>

    <div class="divider"></div>

    <div class="contacts">
      <p class="contact wide">
        <svg viewBox="0 0 20 20" aria-hidden="true"><path d="M10 2 1 10h3v8h5v-5h2v5h5v-8h3z"/></svg>
        Address line one address line one address line one
      </p>
      <p class="contact">
        <svg viewBox="0 0 20 20" aria-hidden="true"><path d="M1 4h18v12H1z M2 5l8 6 8-6" fill="var(--blue)"/></svg>
        email@website.com
      </p>
      <p class="contact">
        <svg viewBox="0 0 20 20" aria-hidden="true"><path d="M5 2l9 7-4 1 3 6-2 1-3-6-3 3z"/></svg>
        www.website.com
      </p>
      <p class="contact">
        <svg viewBox="0 0 20 20" aria-hidden="true"><path d="M6 1h8a1 1 0 0 1 1 1v16a1 1 0 0 1-1 1H6a1 1 0 0 1-1-1V2a1 1 0 0 1 1-1zm1 2v12h6V3z"/></svg>
        123 456 789
      </p>
      <p class="contact">
        <svg viewBox="0 0 20 20" aria-hidden="true"><path d="M5 1h10v5H5zM2 7h16v8h-3v4H5v-4H2zm5 6v4h6v-4z"/></svg>
        123 456 789
      </p>
    </div>
  </section>

</main>
</body>
</html>
```